Tending Our Garden eBook Cover Design

I want to deisgn a cover for my eBook (FRONT COVER) and the title is:

Under the Willow Tree; Where I Found My Quiet Strength and Where You Might Too
By KT Dorran

TITLE CHANGED TO: UNDER THE WILLOW TREE; WHERE I FOUND MY QUIET STRENGTH AND WHERE YOU MIGHT TOO

The color palette is attached. Along with some photos options of me. Along with the ebook in WORD Document. My website is www.KTDorranLive.example. You can use a different color palette if you think it is best

Target Market(s)

women who look to build a personal brand

Industry/Entity Type

health and wellness

Requirements
Must have
• the title
Nice to have
• use my picture on the cover; but that is optional
Should not have
• any men

```html
<!DOCTYPE html>
<html lang="en">
<head>
<meta charset="utf-8">
<title>Under the Willow Tree — KT Dorran</title>
<link rel="stylesheet" href="https://fonts.googleapis.com/css2?family=Playfair+Display:wght@700;800&family=Montserrat:wght@600&display=swap">
<style>
  :root {
    --page: #ffffff;
    --cover: #f0e8e2;
    --gold-dark: #4f3a12;
    --gold-light: #b57a4c;
    --rose-dark: #8a433b;
    --rose-light: #cd776a;
    --ink: #111111;
    --rule: #d3a59c;
  }
  html, body {
    margin: 0;
    width: 1200px;
    height: 1200px;
    overflow: hidden;
    background: var(--page);
  }
  .cover {
    position: absolute;
    left: 156px;
    top: 156px;
    width: 897px;
    height: 900px;
    background: var(--cover);
  }
  .title {
    position: absolute;
    left: 0;
    right: 0;
    top: 70px;
    margin: 0;
    text-align: center;
    font-family: "Playfair Display", serif;
    font-weight: 800;
    letter-spacing: -0.04em;
  }
  .title span {
    display: block;
    padding: 0 20px 40px;
    margin-bottom: -40px;
    -webkit-background-clip: text;
    background-clip: text;
    color: transparent;
  }
  .title .lead {
    font-size: 130px;
    line-height: 140px;
    background-image: linear-gradient(180deg, var(--gold-dark) 0%, var(--gold-dark) 35%, var(--gold-light) 65%, var(--gold-light) 100%);
  }
  .title .main {
    font-size: 175px;
    line-height: 165px;
    background-image: radial-gradient(ellipse 60% 80% at 55% 45%, var(--rose-light) 0%, var(--rose-dark) 100%);
  }
  .subtitle {
    position: absolute;
    left: 120px;
    right: 120px;
    top: 568px;
    margin: 0;
    text-align: center;
    font-family: "Montserrat", sans-serif;
    font-weight: 600;
    font-size: 20px;
    line-height: 30px;
    letter-spacing: 0.08em;
    color: var(--ink);
  }
  .divider {
    position: absolute;
    left: 253px;
    width: 391px;
    top: 652px;
    height: 1px;
    background: var(--rule);
  }
  .author {
    position: absolute;
    left: 0;
    right: 0;
    top: 668px;
    margin: 0;
    text-align: center;
    font-family: "Playfair Display", serif;
    font-weight: 700;
    font-size: 56px;
    line-height: 80px;
    letter-spacing: -0.01em;
    color: var(--ink);
  }
</style>
</head>
<body>
  <main class="cover">
    <h1 class="title">
      <span class="lead">under the</span>
      <span class="main">willow</span>
      <span class="main">tree.</span>
    </h1>
    <p class="subtitle">WHERE I FOUND MY QUIET STRENGTH<br>AND WHERE YOU MIGHT TOO</p>
    <div class="divider"></div>
    <p class="author">KT Dorran</p>
  </main>
</body>
</html>
```